Business Card Design

Design new business card using new logo attached and some details as old business card, which is also attached.

Industry/Entity Type

Business

```html
<!DOCTYPE html>
<html lang="en">
<head>
<meta charset="utf-8">
<title>Whitford Business Card</title>
<link rel="stylesheet" href="https://fonts.googleapis.com/css2?family=Cinzel:wght@400&family=Questrial&display=swap">
<style>
  :root {
    --navy: #25246e;
    --navy-deep: #1d1c5c;
    --grey: #8a8a8f;
    --grey-light: #b8b8c0;
    --paper: #f7f7f8;
    --stage: #2b2b2d;
    --badge: #a9c3e2;
    --band-text: #d9d9e6;
  }
  * { margin: 0; padding: 0; box-sizing: border-box; }
  html, body { width: 1200px; height: 900px; overflow: hidden; }
  body {
    background: var(--stage);
    display: flex;
    flex-direction: column;
    align-items: center;
    justify-content: center;
    gap: 36px;
    font-family: "Questrial", sans-serif;
  }
  .card {
    width: 700px;
    height: 400px;
    position: relative;
    overflow: hidden;
  }

  /* Back side */
  .card-back {
    background: var(--navy);
    display: flex;
    align-items: center;
    justify-content: center;
  }
  .firm-name {
    display: flex;
    align-items: center;
    font-family: "Questrial", sans-serif;
    font-weight: 400;
    line-height: 1;
  }
  .card-back .firm-name { gap: 18px; font-size: 64px; color: #ffffff; }
  .card-back .name-square { width: 26px; height: 26px; background: var(--grey); }

  /* Front side */
  .card-front { background: var(--paper); }
  .identity {
    position: absolute;
    left: 40px; top: 70px;
    display: flex;
    align-items: center;
  }
  .card-front .firm-name {
    gap: 10px;
    font-size: 36px;
    color: var(--navy);
    padding-right: 16px;
  }
  .card-front .name-square { width: 16px; height: 16px; background: var(--grey); }
  .identity-divider {
    width: 1px; height: 70px;
    background: var(--grey-light);
    margin-right: 14px;
  }
  .tagline {
    font-family: "Cinzel", serif;
    color: var(--navy);
    font-size: 17px;
    line-height: 1.1;
  }
  .tagline .firm-principal {
    display: block;
    color: var(--grey);
    font-size: 11px;
    letter-spacing: 1.5px;
    margin-top: 3px;
  }
  .contact {
    position: absolute;
    left: 250px; top: 180px;
    color: var(--navy);
  }
  .contact .person { font-size: 22px; letter-spacing: 0.5px; margin-bottom: 14px; }
  .phones { display: grid; grid-template-columns: 70px auto; font-size: 17px; line-height: 1.2; margin-bottom: 16px; }
  .phones .label { color: var(--grey); }
  .web { font-size: 17px; line-height: 1.25; }
  .member-badge {
    position: absolute;
    left: 44px; top: 258px;
    width: 130px; height: 50px;
  }
  .address-band {
    position: absolute;
    left: 0; right: 0; bottom: 0;
    height: 50px;
    background: var(--navy-deep);
    color: var(--band-text);
    font-size: 17px;
    letter-spacing: 0.5px;
    display: flex;
    align-items: center;
    padding-left: 40px;
  }
</style>
</head>
<body>
  <section class="card card-back" aria-label="Card back">
    <div class="firm-name">
      <span class="name-square"></span>
      <span>Whitford</span>
    </div>
  </section>

  <section class="card card-front" aria-label="Card front">
    <div class="identity">
      <div class="firm-name">
        <span class="name-square"></span>
        <span>Whitford</span>
      </div>
      <div class="identity-divider"></div>
      <div class="tagline">
        Tax, Accounting &amp;<br>Advisory Services
        <span class="firm-principal">Daniel R. Whitford, CPA, PA</span>
      </div>
    </div>

    <div class="contact">
      <p class="person">Dan Whitford, CPA, CVA</p>
      <div class="phones">
        <span class="label">office</span><span>(555) 014-2290</span>
        <span class="label">mobile</span><span>(555) 019-4471</span>
      </div>
      <p class="web">dan@drwcpapa.com<br>www.drwcpapa.com</p>
    </div>

    <svg class="member-badge" viewBox="0 0 130 50" role="img" aria-label="Professional association membership badge">
      <rect x="5" y="8" width="120" height="34" rx="17" fill="var(--badge)"/>
    </svg>

    <div class="address-band">240 Harbor Light Ave., Seabrook Shores, FL 32999</div>
  </section>
</body>
</html>
```